Nutrition center for loss weight

we provide nutritional consulting for loss weight and changing food habits. The clinic is promoting the life healthy, as well as natural and balanced diets that help in the control weight and for the treatment to diseases.

Reason: Waiting some desings.

Reason: Waiting some designers

Reason: Waiting for changes.

Target Market(s)

Mostly women and men aged 30-55, both with overweight, obesity and problems with your food habits.

Industry/Entity Type

Weight

Font styles to use
Script

Colors
cadf82
ffc214
b868aa
f68d4d
0393ce
33b7a4
acd037
cbdf83
eaf2cf

Requirements
Must have
• lively and natural colors
logo that evokes healthy weight, concept of healthy natural food
Nice to have
• Slim fit image with a elegant and simple design
Should not have
• Preferably not used photograps, old-Style, Boring colors

```html
<!DOCTYPE html>
<html lang="en">
<head>
<meta charset="utf-8">
<title>Verdant Nutrition – Business Card</title>
<link href="https://fonts.googleapis.com/css2?family=Oswald:wght@400;500&display=swap" rel="stylesheet">
<style>
  :root {
    --page: #ffffff;
    --paper: #f5f2ea;
    --mint: #93cdb4;
    --mint-light: #a9d9c3;
    --mint-dark: #5ea786;
    --earth: #8f7d73;
    --earth-text: #8a7a70;
    --white: #ffffff;
  }
  * { margin: 0; padding: 0; box-sizing: border-box; }
  html, body {
    width: 1200px; height: 1200px; overflow: hidden;
    background: var(--page);
    font-family: "Oswald", "Arial Narrow", sans-serif;
  }
  .card {
    position: absolute; left: 220px;
    width: 760px; height: 434px;
    background: var(--paper);
    box-shadow: 0 6px 18px rgba(0,0,0,0.15);
    overflow: hidden;
  }
  .card--front { top: 110px; }
  .card--back { top: 640px; }

  /* Front */
  .front-band {
    position: absolute; left: 0; right: 0; top: 200px; height: 52px;
    background: var(--mint-light);
  }
  .front-ribbon {
    position: absolute; left: 150px; top: 185px; width: 460px; height: 76px;
    background: var(--mint);
    display: flex; align-items: center; justify-content: center;
  }
  .front-fold { position: absolute; top: 261px; }
  .front-fold--left { left: 150px; }
  .front-fold--right { left: 584px; }
  .brand-name {
    color: var(--white); font-weight: 400; font-size: 44px; letter-spacing: 2px;
  }
  .food-illustration {
    position: absolute; left: 250px; top: 100px; width: 260px; height: 86px;
    border-radius: 40px 40px 8px 8px;
    background: linear-gradient(90deg, #c98a55, #f08a3c, #6aa84f, #e0b040, #4f9a4a, #9aa8b8, #b08560, #f2b233);
  }

  /* Back */
  .earth-strip {
    position: absolute; left: 0; top: 0; bottom: 0; width: 240px;
    background: var(--earth);
  }
  .info-ribbon {
    position: absolute; left: 0; width: 370px; height: 72px;
    background: var(--mint);
    display: flex; align-items: center; padding-left: 26px;
    color: var(--white); font-weight: 500; font-size: 33px; letter-spacing: 0.5px;
  }
  .info-fold { position: absolute; left: 342px; }
  .info-ribbon--name { top: 70px; }
  .info-ribbon--tel { top: 176px; }
  .info-ribbon--web { top: 282px; }
  .info-fold--name { top: 142px; }
  .info-fold--tel { top: 248px; }
  .info-fold--web { top: 354px; }
  .address {
    position: absolute; left: 400px; right: 20px; top: 168px;
    text-align: center; color: var(--earth-text);
    font-weight: 500; font-size: 36px; line-height: 1.25; letter-spacing: 0.5px;
  }
</style>
</head>
<body>
  <section class="card card--front">
    <div class="front-band"></div>
    <div class="food-illustration" role="img" aria-label="Illustration of fresh foods: bread, carrot, broccoli, pineapple, watermelon, fish, coconut and juice"></div>
    <div class="front-ribbon"><span class="brand-name">Verdant Nutrition</span></div>
    <svg class="front-fold front-fold--left" width="26" height="16" viewBox="0 0 26 16"><polygon points="0,0 26,0 26,16" fill="var(--mint-dark)"/></svg>
    <svg class="front-fold front-fold--right" width="26" height="16" viewBox="0 0 26 16"><polygon points="0,0 26,0 0,16" fill="var(--mint-dark)"/></svg>
  </section>

  <section class="card card--back">
    <div class="earth-strip"></div>
    <div class="info-ribbon info-ribbon--name">NAME : XXXXXX</div>
    <svg class="info-fold info-fold--name" width="28" height="18" viewBox="0 0 28 18"><polygon points="0,0 28,0 0,18" fill="var(--mint-dark)"/></svg>
    <div class="info-ribbon info-ribbon--tel">TEL : XXXXX . XXXXX</div>
    <svg class="info-fold info-fold--tel" width="28" height="18" viewBox="0 0 28 18"><polygon points="0,0 28,0 0,18" fill="var(--mint-dark)"/></svg>
    <div class="info-ribbon info-ribbon--web">WEB SITE : WWW.XX.XX</div>
    <svg class="info-fold info-fold--web" width="28" height="18" viewBox="0 0 28 18"><polygon points="0,0 28,0 0,18" fill="var(--mint-dark)"/></svg>
    <address class="address" style="font-style:normal">
      OLMO Nº27<br>
      COL. ARBOLEDAS<br>
      VALLE VERDE - MÉXICO
    </address>
  </section>
</body>
</html>
```